Bramblewick Gardening Services. A6 flyer single sided

Need an A6 flyer designing. Single sided.
I am a gardener.
I do lawn mowing - one-off garden tidy ups or regular fortnightly visits.
All kinds of trees expertly felled, topped or pruned.
Hedge cutting.
Fencing replaced or repaired.
Fully insured.
Access to fully qualified and licenced tree arborist
07724 316048 or 01632 742918.

I have attached my business card and letter head logo.
I'm open to new designs without incorporating any of my artwork.

Industry/Entity Type

Gardener

```html
<!DOCTYPE html>
<html lang="en">
<head>
<meta charset="utf-8">
<title>Bramblewick Gardening Services – Flyer</title>
<link href="https://fonts.googleapis.com/css2?family=Tinos:wght@400;700&display=swap" rel="stylesheet">
<style>
  :root {
    --leaf: #4ba339;
    --leaf-dark: #2f7d2a;
    --leaf-light: #8cc63f;
    --ink: #111111;
    --paper: #ffffff;
    --sky: #cfe3d2;
    --lawn: #5e9a32;
  }
  html, body {
    margin: 0;
    padding: 0;
    overflow: hidden;
    background: #e9e9e9;
  }
  .flyer {
    position: relative;
    width: 853px;
    height: 1200px;
    overflow: hidden;
    background: var(--paper);
    font-family: "Tinos", "Times New Roman", serif;
  }
  .backdrop {
    position: absolute;
    inset: 0;
    width: 853px;
    height: 1200px;
  }
  .headline {
    position: absolute;
    left: 0;
    top: 0;
    width: 470px;
    height: 213px;
    background: var(--leaf);
    color: var(--paper);
    font-weight: 700;
    font-size: 58px;
    line-height: 70px;
    letter-spacing: 1px;
    padding: 34px 0 0 30px;
    box-sizing: border-box;
    margin: 0;
  }
  .services-panel {
    position: absolute;
    left: 0;
    top: 560px;
    width: 384px;
    height: 640px;
    background: var(--leaf);
    color: var(--paper);
    font-weight: 700;
    font-size: 45px;
    line-height: 62px;
    text-align: center;
    padding-top: 38px;
    box-sizing: border-box;
    margin: 0;
  }
  .details {
    position: absolute;
    left: 400px;
    width: 453px;
    text-align: center;
    color: var(--ink);
    font-weight: 700;
    margin: 0;
  }
  .trees {
    top: 758px;
    font-size: 31px;
    line-height: 34px;
  }
  .hedge {
    top: 892px;
    font-size: 44px;
    line-height: 48px;
    color: var(--leaf-dark);
  }
  .fencing {
    top: 955px;
    font-size: 31px;
    line-height: 34px;
  }
  .arborist {
    position: absolute;
    left: 406px;
    top: 1068px;
    width: 432px;
    height: 118px;
    background: var(--leaf-dark);
    color: var(--paper);
    font-weight: 700;
    font-size: 22px;
    line-height: 31px;
    text-align: center;
    padding-top: 13px;
    box-sizing: border-box;
    margin: 0;
  }
</style>
</head>
<body>
  <main class="flyer">
    <svg class="backdrop" viewBox="0 0 853 1200" xmlns="http://www.w3.org/2000/svg">
      <defs>
        <linearGradient id="garden-tones" x1="0" y1="0" x2="0" y2="1">
          <stop offset="0" stop-color="#d9e8d6"/>
          <stop offset="0.35" stop-color="#9cc37a"/>
          <stop offset="0.7" stop-color="#5e9a32"/>
          <stop offset="1" stop-color="#3f7d22"/>
        </linearGradient>
      </defs>
      <rect class="garden-photo" x="0" y="0" width="853" height="780" fill="url(#garden-tones)" role="img" aria-label="Photo of a petrol lawn mower on a freshly cut lawn with a garden play house behind"/>
      <path class="wave-white" d="M0 560 C 250 700, 520 700, 853 620 L 853 1200 L 0 1200 Z" fill="var(--paper)"/>
      <path class="wave-band" d="M0 520 C 250 660, 520 670, 853 585 L 853 615 C 520 700, 250 690, 0 560 Z" fill="var(--leaf-light)"/>
      <path class="wave-line" d="M0 575 C 260 715, 540 715, 853 640" fill="none" stroke="var(--leaf)" stroke-width="6"/>
    </svg>

    <h1 class="headline">I AM A<br>GARDENER</h1>

    <p class="services-panel">I do lawn<br>mowing<br>- one-off<br>garden<br>tidy ups<br>or regular<br>fortnightly<br>visits.</p>

    <p class="details trees">All kinds of trees<br>expertly felled,<br>topped or pruned.</p>
    <p class="details hedge">Hedge Cutting</p>
    <p class="details fencing">Fencing replaced or<br>repaired. Fully insured.</p>

    <p class="arborist">Access to fully qualified<br>and licenced tree arborist<br>07724 316048 or 01632 742918</p>
  </main>
</body>
</html>
```